Corporate Business Cards

We need a new design for all of our business cards. They are boring and need some life.

Industry/Entity Type

Business

Requirements
Must have
• Corporate Logo of some type (See attached Pyramid)

Corporate Phrase "Accelerating Cashflow"

```html
<!DOCTYPE html>
<html lang="en">
<head>
<meta charset="utf-8">
<title>Meridian Ledger – Business Cards</title>
<link rel="stylesheet" href="https://fonts.googleapis.com/css2?family=Libre+Baskerville:wght@400;700&display=swap">
<style>
  :root {
    --page-bg: #ecebe6;
    --lavender: #bebee0;
    --navy: #44478f;
    --navy-light: #5256a6;
    --white: #ffffff;
    --card-shadow: rgba(30, 30, 60, 0.18);
  }
  * { box-sizing: border-box; margin: 0; padding: 0; }
  html, body {
    width: 1200px;
    height: 762px;
    overflow: hidden;
    background: var(--page-bg);
    font-family: "Libre Baskerville", "Times New Roman", serif;
  }
  .canvas {
    width: 1200px;
    height: 762px;
    display: flex;
    align-items: center;
    justify-content: center;
    gap: 50px;
  }
  .card {
    position: relative;
    width: 540px;
    height: 309px;
    overflow: hidden;
    background: linear-gradient(135deg, var(--navy) 0%, var(--navy-light) 100%);
    box-shadow: 0 10px 28px var(--card-shadow);
    color: var(--white);
  }
  .card__band {
    position: absolute;
    left: 0; top: 0;
    width: 100%;
    background: var(--lavender);
  }
  .brand {
    position: absolute;
    display: flex;
    align-items: center;
    gap: 18px;
  }
  .brand__square {
    width: 34px;
    height: 34px;
    background: var(--white);
    flex: none;
  }
  .brand__name {
    font-weight: 400;
    text-transform: uppercase;
    color: var(--white);
    line-height: 1.05;
    letter-spacing: 0.02em;
    white-space: nowrap;
  }

  /* Front */
  .card--front .card__band { height: 44%; }
  .card--front .brand { left: 60px; top: 92px; }
  .card--front .brand__name { font-size: 40px; }
  .tagline {
    position: absolute;
    right: 36px;
    bottom: 30px;
    font-size: 14px;
    font-weight: 400;
    letter-spacing: 0.16em;
    text-transform: uppercase;
    color: var(--white);
    white-space: nowrap;
  }

  /* Back */
  .card--back .card__band { height: 26%; }
  .card--back .brand { left: 28px; top: 22px; gap: 10px; }
  .card--back .brand__square { width: 18px; height: 18px; }
  .card--back .brand__name { font-size: 18px; }
  .card__rule {
    position: absolute;
    left: 0;
    right: 0;
    top: 26%;
    height: 2px;
    background: var(--white);
  }
  .contact {
    position: absolute;
    left: 56px;
    top: 118px;
    font-size: 17px;
    line-height: 1.45;
    white-space: nowrap;
  }
  .contact__role { margin-bottom: 30px; }
</style>
</head>
<body>
  <main class="canvas">
    <section class="card card--back" aria-label="Business card back">
      <div class="card__band"></div>
      <div class="brand">
        <span class="brand__square"></span>
        <span class="brand__name">Meridian<br>Ledger</span>
      </div>
      <div class="card__rule"></div>
      <div class="contact">
        <p class="contact__name">Your name</p>
        <p class="contact__role">Position</p>
        <p class="contact__line">Address: 12 Harbor Street, Suite 4</p>
        <p class="contact__line">Phone: 555 0142 0198</p>
      </div>
    </section>

    <section class="card card--front" aria-label="Business card front">
      <div class="card__band"></div>
      <div class="brand">
        <span class="brand__square"></span>
        <span class="brand__name">Meridian<br>Ledger</span>
      </div>
      <p class="tagline">Accelerating Cashflow</p>
    </section>
  </main>
</body>
</html>
```